A boutique/architectural website for a landscape company

I'm after a minimilstic boutique website for my landscape design and construction business. I have been exploring Wix and created some pages on that but want something more aesthetic.

Industry/Entity Type

Landscaping design and construction

Number of Pages Required

5+ page

Font styles to use
Sans Serif

Colors

Designer to choose colors to be used in the design.

Requirements
Must have
• an architectural, minimalistic look
Nice to have
• Simplicitly and nice images
Should not have
• A corporate look

```html
<!DOCTYPE html>
<html lang="en">
<head>
<meta charset="utf-8">
<title>Ridgeline Landscaping</title>
<link href="https://fonts.googleapis.com/css2?family=Roboto:wght@400;500;700&display=swap" rel="stylesheet">
<style>
:root{
  --green-deep:#0f3d33;
  --green-news:#173f37;
  --sage:#b7cab1;
  --sage-light:#cfdcca;
  --ink:#111;
  --muted:#8a8a8a;
  --footer:#2b2b2b;
  --white:#fff;
  --field:#f6f6f6;
}
*{margin:0;padding:0;box-sizing:border-box}
html,body{width:1200px;height:3897px;overflow:hidden}
body{position:relative;font-family:'Roboto',sans-serif;color:var(--ink);background:var(--white)}
.abs{position:absolute}
.center{text-align:center}
.topline{left:0;top:0;width:1200px;height:5px;background:var(--sage)}
.nav{left:0;top:5px;width:1200px;height:67px;background:var(--white)}
.nav-link{font-size:15px;color:#222;letter-spacing:.2px}
.brand-badge{left:113px;top:12px;width:118px;height:118px;border-radius:50%;background:var(--green-deep);border:5px solid var(--white);box-shadow:0 2px 6px rgba(0,0,0,.25);z-index:3;display:flex;align-items:center;justify-content:center;color:var(--white);font-weight:700;font-size:14px;letter-spacing:1px}
.social-dot{width:12px;height:12px;border-radius:50%;background:#222}
.hero{left:0;top:72px;width:1200px;height:604px;background:linear-gradient(180deg,#a7b69a 0%,#8ea47a 35%,#6e9a3e 65%,#4f7d2a 100%)}
.hero-title{left:0;top:278px;width:1200px;font-size:42px;font-weight:700;color:var(--white);letter-spacing:.5px}
.hero-text{left:300px;top:350px;width:600px;font-size:15px;line-height:25px;color:var(--white)}
.btn{display:flex;align-items:center;justify-content:center;gap:10px;border-radius:30px;font-weight:700;font-size:15px;color:var(--white)}
.btn-arrow{width:14px;height:14px}
.hero-btn{left:510px;top:431px;width:180px;height:46px;background:#b9c9a4;color:#123}
.slide-arrow{top:371px;width:24px;height:24px;background:rgba(255,255,255,.25);border-radius:3px}
h2.section-title{position:absolute;left:0;width:1200px;text-align:center;font-size:38px;font-weight:700;letter-spacing:.5px}
.underline{height:3px;width:56px;background:var(--green-deep)}
.about-text{left:100px;top:890px;width:492px;font-size:15px;line-height:25.7px;text-align:center;color:#222}
.photo{box-shadow:0 3px 10px rgba(0,0,0,.25);border:3px solid var(--white)}
.services{left:0;top:1268px;width:1200px;height:525px;background:var(--sage-light)}
.card{top:1418px;width:283px;height:323px;background:var(--white);box-shadow:0 2px 8px rgba(0,0,0,.15)}
.card-img{left:0;top:0;width:283px;height:156px}
.card-title{left:0;top:172px;width:283px;text-align:center;font-weight:700;font-size:15px}
.card-text{left:18px;top:204px;width:247px;text-align:center;font-size:15px;line-height:25.5px;color:var(--muted)}
.read-more{display:flex;align-items:center;gap:8px;font-weight:700;font-size:15px;color:var(--green-deep)}
.news{left:0;top:2531px;width:1200px;height:439px;background:var(--green-news)}
.news-card{top:2708px;width:488px;height:197px;background:var(--white)}
.news-img{left:0;top:0;width:190px;height:197px}
.news-title{left:213px;top:22px;font-weight:700;font-size:15px;letter-spacing:.3px}
.news-meta{left:213px;top:52px;font-size:13px;color:#b5c2a8;display:flex;gap:30px}
.news-text{left:213px;top:78px;width:258px;font-size:13.5px;line-height:22.5px;color:var(--muted)}
.field{background:var(--field);border:1px solid #ddd;font-size:13px;padding:0 14px;display:flex;align-items:center;color:#222}
.footer{left:0;top:3465px;width:1200px;height:432px;background:var(--footer);color:var(--white)}
.foot-head{top:144px;font-weight:700;font-size:14px;letter-spacing:.3px}
.foot-link{font-size:14.5px;display:flex;gap:10px}
.icon-ring{width:32px;height:32px;border:1.5px solid var(--white);border-radius:50%;display:flex;align-items:center;justify-content:center}
.soc-ring{top:340px;width:30px;height:30px;border:1.5px solid var(--white);border-radius:50%}
</style>
</head>
<body>
<div class="abs topline"></div>
<header class="abs nav">
  <div class="abs nav-link" style="left:300px;top:25px">HOME</div>
  <div class="abs nav-link" style="left:383px;top:25px">ABOUT US</div>
  <div class="abs nav-link" style="left:501px;top:25px">SERVICES</div>
  <div class="abs nav-link" style="left:617px;top:25px">GALLERY</div>
  <div class="abs nav-link" style="left:726px;top:25px">BLOG</div>
  <div class="abs nav-link" style="left:808px;top:25px">CONTACT US</div>
  <div class="abs social-dot" style="left:941px;top:28px"></div>
  <div class="abs social-dot" style="left:977px;top:28px"></div>
  <div class="abs social-dot" style="left:1015px;top:28px"></div>
  <svg class="abs" style="left:1071px;top:26px" width="16" height="16" viewBox="0 0 16 16"><circle cx="6.5" cy="6.5" r="5" fill="none" stroke="#111" stroke-width="2"/><line x1="10.5" y1="10.5" x2="15" y2="15" stroke="#111" stroke-width="2.4"/></svg>
</header>
<div class="abs brand-badge">RIDGELINE</div>

<section class="abs hero" role="img" aria-label="Photo of a landscaped front garden with a large tree, curved stone path, lawn and white house"></section>
<div class="abs hero-title center">RIDGELINE LANDSCAPING</div>
<p class="abs hero-text center">Lorem ipsum dolor sit amet, consectetur adipiscing elit, sed do eiusmod tempor incididunt ut labore et dolore magna aliqua. Ut enim ad minim veniam, quis nostrud.</p>
<div class="abs btn hero-btn">GET STARTED <svg class="btn-arrow" viewBox="0 0 14 14"><circle cx="7" cy="7" r="7" fill="#123"/><path d="M5.5 4l3 3-3 3" stroke="#b9c9a4" stroke-width="1.8" fill="none"/></svg></div>
<svg class="abs slide-arrow" style="left:47px" viewBox="0 0 24 24"><path d="M18 12H6M10 8l-4 4 4 4" stroke="#fff" stroke-width="2" fill="none"/></svg>
<svg class="abs slide-arrow" style="left:1127px" viewBox="0 0 24 24"><path d="M6 12h12M14 8l4 4-4 4" stroke="#fff" stroke-width="2" fill="none"/></svg>

<h2 class="section-title" style="left:-254px;top:812px">ABOUT US</h2>
<div class="abs underline" style="left:318px;top:862px"></div>
<p class="abs about-text">Lorem ipsum dolor sit amet, consectetur adipiscing elit, sed do eiusmod tempor incididunt ut labore et dolore magna aliqua. Ut enim ad minim veniam, quis nostrud exercitation ullamco labris nisi ut aliquip ex ea commodo consequat. Duis aute irure dolor in reprehenderit in voluptate velit esse cillum dolore Duis aute irure dolor in reprehenderit in voluptate eu fugiat nulla pariatur.</p>
<div class="abs btn" style="left:256px;top:1071px;width:181px;height:49px;background:var(--green-deep)">LEARN MORE <svg class="btn-arrow" viewBox="0 0 14 14"><circle cx="7" cy="7" r="7" fill="#fff"/><path d="M5.5 4l3 3-3 3" stroke="#0f3d33" stroke-width="1.8" fill="none"/></svg></div>
<div class="abs photo" style="left:638px;top:812px;width:401px;height:370px;background:linear-gradient(180deg,#d9dde0 0%,#b9bdb6 45%,#6f9a3e 75%,#5a8a30 100%)" role="img" aria-label="Photo of an apartment building beside a mown lawn"></div>
<div class="abs photo" style="left:840px;top:761px;width:284px;height:251px;background:linear-gradient(180deg,#8eb3da 0%,#5a6e86 45%,#6f8a5a 75%,#7a7e80 100%)" role="img" aria-label="Photo of a blue house with a stone patio and flower beds"></div>

<section class="abs services" role="img" aria-label="Faded background photo of a house and lawn"></section>
<h2 class="section-title" style="top:1310px">OUR SERVICES</h2>
<div class="abs underline" style="left:572px;top:1364px"></div>

<div class="abs card" style="left:145px"><div class="abs card-img" style="background:linear-gradient(180deg,#6d9fd4,#3a5f8a 60%,#5f8a3d)" role="img" aria-label="Photo of glass towers with landscaped grounds"></div><div class="abs card-title">Lorem ipsum dolor sit amet</div><p class="abs card-text">Sed ut perspiciatis unde omnis iste natus error sit voluptatem loremque laudantium, totam rem aperiam.</p><div class="abs read-more" style="left:88px;top:287px">READ MORE <svg width="14" height="14" viewBox="0 0 14 14"><circle cx="7" cy="7" r="7" fill="#0f3d33"/><path d="M5.5 4l3 3-3 3" stroke="#fff" stroke-width="1.8" fill="none"/></svg></div></div>
<div class="abs card" style="left:463px"><div class="abs card-img" style="background:linear-gradient(180deg,#a9c7e6,#6f8e4e 45%,#58902f)" role="img" aria-label="Photo of a curved lawn with colourful flower beds"></div><div class="abs card-title">Lorem ipsum dolor sit amet</div><p class="abs card-text">Sed ut perspiciatis unde omnis iste natus error sit voluptatem loremque laudantium, totam rem aperiam.</p><div class="abs read-more" style="left:88px;top:287px">READ MORE <svg width="14" height="14" viewBox="0 0 14 14"><circle cx="7" cy="7" r="7" fill="#0f3d33"/><path d="M5.5 4l3 3-3 3" stroke="#fff" stroke-width="1.8" fill="none"/></svg></div></div>
<div class="abs card" style="left:772px"><div class="abs card-img" style="background:linear-gradient(180deg,#c4d8ea,#6a6e6a 45%,#5e9a34)" role="img" aria-label="Photo of suburban houses with green lawns"></div><div class="abs card-title">Lorem ipsum dolor sit amet</div><p class="abs card-text">Sed ut perspiciatis unde omnis iste natus error sit voluptatem loremque laudantium, totam rem aperiam.</p><div class="abs read-more" style="left:88px;top:287px">READ MORE <svg width="14" height="14" viewBox="0 0 14 14"><circle cx="7" cy="7" r="7" fill="#0f3d33"/><path d="M5.5 4l3 3-3 3" stroke="#fff" stroke-width="1.8" fill="none"/></svg></div></div>

<h2 class="section-title" style="top:1871px">OUR GALLERY</h2>
<div class="abs underline" style="left:572px;top:1925px"></div>
<div class="abs" style="left:174px;top:1974px;width:257px;height:282px;background:linear-gradient(180deg,#4a7fc0,#2e4e78 55%,#6aa83c)" role="img" aria-label="Photo of glass towers above a lawn"></div>
<div class="abs" style="left:174px;top:2273px;width:257px;height:171px;background:linear-gradient(180deg,#cfe0ee,#9c8c70 40%,#6aa83c)" role="img" aria-label="Photo of houses across a wide lawn"></div>
<div class="abs" style="left:449px;top:1974px;width:303px;height:202px;background:linear-gradient(180deg,#a59378,#6e6a5e 50%,#5e9a34)" role="img" aria-label="Photo of a brick house entrance with hedges"></div>
<div class="abs" style="left:449px;top:2194px;width:303px;height:250px;background:linear-gradient(180deg,#8fb8e4,#9aa08c 40%,#7aa84a 75%,#a8a8a0)" role="img" aria-label="Photo of a garden path between houses"></div>
<div class="abs" style="left:770px;top:1974px;width:257px;height:282px;background:linear-gradient(180deg,#e8eef4,#7a8498 50%,#5e9a34)" role="img" aria-label="Photo of a grey two-storey house with lawn"></div>
<div class="abs" style="left:770px;top:2273px;width:257px;height:171px;background:linear-gradient(180deg,#e6ebe0,#a88a66 45%,#4f8a2a)" role="img" aria-label="Photo of a stone retaining wall with plants"></div>

<section class="abs news" role="img" aria-label="Dark green tinted photo of a garden"></section>
<h2 class="section-title" style="top:2586px;color:var(--white)">OUR NEWS</h2>
<div class="abs underline" style="left:572px;top:2640px;background:var(--white)"></div>
<article class="abs news-card" style="left:98px"><div class="abs news-img" style="background:linear-gradient(180deg,#8a7a6a,#9a9484 45%,#5e9a34)" role="img" aria-label="Photo of terraced garden walls"></div><div class="abs news-title">LOREM IPSUM DOLOR AMET</div><div class="abs news-meta"><span>▦ 17.7.2021</span><span>◁ Share</span></div><p class="abs news-text">Sed ut perspiciatis unde natus error sit voluptatem accusantium doloremque laudantium, totam rem aperiam, eaque</p><div class="abs read-more" style="left:213px;top:156px">READ MORE <svg width="14" height="14" viewBox="0 0 14 14"><circle cx="7" cy="7" r="7" fill="#0f3d33"/><path d="M5.5 4l3 3-3 3" stroke="#fff" stroke-width="1.8" fill="none"/></svg></div></article>
<article class="abs news-card" style="left:614px"><div class="abs news-img" style="background:linear-gradient(180deg,#5e8fd0,#aab4be 45%,#5e9a34)" role="img" aria-label="Photo of a white house with front lawn"></div><div class="abs news-title">LOREM IPSUM DOLOR AMET</div><div class="abs news-meta"><span>▦ 17.7.2021</span><span>◁ Share</span></div><p class="abs news-text">Sed ut perspiciatis unde natus error sit voluptatem accusantium doloremque laudantium, totam rem aperiam, eaque</p><div class="abs read-more" style="left:213px;top:156px">READ MORE <svg width="14" height="14" viewBox="0 0 14 14"><circle cx="7" cy="7" r="7" fill="#0f3d33"/><path d="M5.5 4l3 3-3 3" stroke="#fff" stroke-width="1.8" fill="none"/></svg></div></article>

<h2 class="section-title" style="top:3047px">GET N TOUCH</h2>
<div class="abs underline" style="left:572px;top:3101px"></div>
<div class="abs field" style="left:251px;top:3136px;width:348px;height:34px">First Name:</div>
<div class="abs field" style="left:611px;top:3136px;width:338px;height:34px">Email:</div>
<div class="abs field" style="left:251px;top:3188px;width:348px;height:36px">Phone Number:</div>
<div class="abs field" style="left:611px;top:3188px;width:338px;height:36px">Address:</div>
<div class="abs field" style="left:251px;top:3238px;width:698px;height:79px;align-items:flex-start;padding-top:12px">Message:</div>
<div class="abs btn" style="left:533px;top:3347px;width:133px;height:41px;background:var(--green-deep)">SUBMIT <svg class="btn-arrow" viewBox="0 0 14 14"><circle cx="7" cy="7" r="7" fill="#fff"/><path d="M4 7l6-3-2 6-1-2z" fill="#0f3d33"/></svg></div>

<footer class="abs footer">
  <div class="abs" style="left:218px;top:38px;font-weight:700;font-size:17px">SIGN UP FOR NEWSLETTER</div>
  <div class="abs" style="left:513px;top:25px;width:466px;height:44px;background:var(--white);border:2px solid #dfe6d8"></div>
  <svg class="abs" style="left:532px;top:42px" width="16" height="12" viewBox="0 0 16 12"><rect x="1" y="1" width="14" height="10" fill="none" stroke="#2f7a6a" stroke-width="1.4"/><path d="M1 1l7 6 7-6" fill="none" stroke="#2f7a6a" stroke-width="1.4"/></svg>
  <div class="abs" style="left:562px;top:40px;font-size:12px;color:#222">Enter Your Email:</div>
  <div class="abs" style="left:835px;top:27px;width:142px;height:40px;background:#b8c9ad;display:flex;align-items:center;justify-content:center;font-weight:700;font-size:15px;color:var(--white)">SUBSCRIBE</div>
  <div class="abs" style="left:110px;top:100px;width:978px;height:1px;background:#555"></div>
  <div class="abs" style="left:110px;top:150px;font-weight:700;font-size:22px;letter-spacing:1px">RIDGELINE</div>
  <p class="abs" style="left:110px;top:246px;width:270px;font-size:14.5px;line-height:24.5px">Lorem ipsum dolor consectetur elit, sed do eiusmod tempor incididunt ut labore et dolore magna aliqua.</p>
  <div class="abs soc-ring" style="left:111px"></div><div class="abs soc-ring" style="left:153px"></div><div class="abs soc-ring" style="left:195px"></div><div class="abs soc-ring" style="left:238px"></div>
  <div class="abs foot-head" style="left:457px">QUICKLINKS</div>
  <div class="abs foot-link" style="left:457px;top:175px">» <span>Contact Us</span></div>
  <div class="abs foot-link" style="left:457px;top:209px">» <span>FAQ</span></div>
  <div class="abs foot-link" style="left:457px;top:243px">» <span>Services</span></div>
  <div class="abs foot-link" style="left:457px;top:277px">» <span>Privacy</span></div>
  <div class="abs foot-link" style="left:457px;top:311px">» <span>Policy</span></div>
  <div class="abs foot-head" style="left:649px">QUICKLINKS</div>
  <div class="abs foot-link" style="left:649px;top:175px">» <span>Home</span></div>
  <div class="abs foot-link" style="left:649px;top:209px">» <span>About Us</span></div>
  <div class="abs foot-link" style="left:649px;top:243px">» <span>Services</span></div>
  <div class="abs foot-link" style="left:649px;top:277px">» <span>Gallery</span></div>
  <div class="abs foot-link" style="left:649px;top:311px">» <span>Blog</span></div>
  <div class="abs foot-link" style="left:649px;top:345px">» <span>Contact Us</span></div>
  <div class="abs foot-head" style="left:843px">CONTACT US</div>
  <div class="abs icon-ring" style="left:841px;top:181px"><svg width="14" height="14" viewBox="0 0 14 14"><path d="M3 1l2.5 3-1.5 1.5c1 2 2.5 3.5 4.5 4.5L10 8.5l3 2.5-1.5 2C6 12.5 1.5 8 1 2.5z" fill="none" stroke="#fff" stroke-width="1.2"/></svg></div>
  <div class="abs" style="left:888px;top:189px;font-size:14.5px">555-010-204</div>
  <div class="abs icon-ring" style="left:841px;top:243px"><svg width="14" height="11" viewBox="0 0 14 11"><rect x=".7" y=".7" width="12.6" height="9.6" fill="none" stroke="#fff" stroke-width="1.2"/><path d="M1 1l6 5 6-5" fill="none" stroke="#fff" stroke-width="1.2"/></svg></div>
  <div class="abs" style="left:888px;top:251px;font-size:14.5px">info@ridgelinelandscaping.com</div>
  <div class="abs icon-ring" style="left:841px;top:309px"><svg width="12" height="15" viewBox="0 0 12 15"><path d="M6 14C2 9 1 7 1 5a5 5 0 0110 0c0 2-1 4-5 9z" fill="none" stroke="#fff" stroke-width="1.2"/><circle cx="6" cy="5" r="1.8" fill="#fff"/></svg></div>
  <p class="abs" style="left:888px;top:304px;width:200px;font-size:14.5px;line-height:22px">Lorem ipsum dolor sit amet consectetur adipiscing elit</p>
  <div class="abs center" style="left:0;top:399px;width:1200px;font-size:14.5px">© 2019 Copyrights I Ridgeline Landscaping.com I All Rights Reserved</div>
</footer>
</body>
</html>
```